Valdessa's New Trucking Company Website

We are wanting to create a basic website for “Valdessa Trucking” on www.ValdessaTrucking.example.

The first attachment titled “write-up” has 7 sections listed, which we would like as tabs at the top of the website, followed by the write up of that section. (The sections ‘employment’ and ‘requirements’ should be under one section).

We would like the landing page to be that of a photo of a Valdessa Truck. Please see attachment two “Valdessa_truck” as an example of what our truck looks like. We would like this to be of better quality/more pleasing to the eye. The rest of the attachments (attachment 3- attachment 7) are of possible photos/ideas.

Woould you be able to photoshop any of those trucks to look like our Valdessa Truck on to a pretty highway/background etc?

We would like this main photo be a constant background of the website, even when you click around the website and the language changes.

Target Market(s)

Northwest Based Companies seeking Transportation needs, grocery stores, Truck Drivers

Industry/Entity Type

Trucking Company

Number of Pages Required

5+ page

Font styles to use
Sans Serif

Requirements
Must have
• Must have one really good photo of our truck (or a truck that looks like ours) as the main photo on the page. This photo must stay consistent as the background when people click on the tabs/sections below.
Nice to have
• Clean/simple layout
Should not have
• Dull colors/ disorganized.

```html
<!DOCTYPE html>
<html lang="en">
<head>
<meta charset="utf-8">
<title>Valdessa Trucking</title>
<link rel="stylesheet" href="https://fonts.googleapis.com/css2?family=Open+Sans:wght@400;600;700;800&display=swap">
<style>
:root{
  --red:#d9251d;
  --red-dark:#b81b14;
  --ink:#333333;
  --muted:#666666;
  --light:#f2f2f2;
  --nav:#e4e4e4;
  --dark:#222222;
  --darker:#1a1a1a;
  --footer-text:#bdbdbd;
  --white:#ffffff;
}
*{box-sizing:border-box;margin:0;padding:0}
html,body{width:1200px;height:2368px;overflow:hidden}
body{font-family:"Open Sans",Arial,sans-serif;color:var(--ink);background:var(--white)}

.site-header{height:108px;display:flex;align-items:center;justify-content:space-between;padding:0 60px 0 70px}
.brand{font-weight:700;font-size:34px;color:var(--red);letter-spacing:-.5px}
.main-nav{display:flex;background:var(--nav);border-radius:18px;padding:6px 10px}
.main-nav a{font-size:15px;color:var(--ink);text-decoration:none;padding:6px 14px;border-right:1px solid #c8c8c8}
.main-nav a:last-child{border-right:none}

.hero{position:relative;height:632px;background:linear-gradient(180deg,#5fa6dc 0%,#a9d2f0 42%,#dfeaf2 52%,#6f8f52 60%,#8a8d8f 72%,#5d6164 100%)}
.hero-arrow{position:absolute;top:290px;width:34px;height:52px;background:rgba(0,0,0,.35);display:flex;align-items:center;justify-content:center}
.hero-arrow.prev{left:0}
.hero-arrow.next{right:0}

.section-title{text-align:center;font-weight:700;font-size:30px;color:#555;letter-spacing:.5px}
.section-title::after{content:"";display:block;width:60px;height:3px;background:var(--red);margin:12px auto 0}

.about{height:420px;padding-top:46px}
.about-body{display:flex;gap:40px;padding:44px 90px 0 90px}
.about-text{flex:1;font-size:14px;line-height:1.75;color:var(--muted)}
.about-text p{margin-bottom:18px}
.about-photo{width:420px;height:222px;background:linear-gradient(135deg,#b5582f,#6c7f8f 60%,#d7d9db);flex-shrink:0}

.services{height:420px;background:linear-gradient(180deg,#3b4147,#23272b);display:flex;justify-content:center;gap:110px;padding-top:90px}
.service{width:260px;text-align:center;color:var(--white)}
.service-icon{width:164px;height:164px;border-radius:50%;background:var(--red);border:5px solid rgba(255,255,255,.85);margin:0 auto 22px;display:flex;align-items:center;justify-content:center}
.service h3{font-weight:800;font-size:25px;line-height:1.05;text-transform:uppercase}

.clients{height:280px;padding-top:40px}
.client-row{display:flex;justify-content:space-between;align-items:center;padding:46px 90px 0}
.client{font-weight:700;font-size:20px;color:#555}

.site-footer{height:430px;background:var(--dark);color:var(--footer-text);display:flex;padding:46px 70px 0 80px;gap:70px}
.footer-col h4{color:var(--white);font-size:14px;font-weight:600;text-transform:uppercase;margin-bottom:20px}
.footer-col h4::after{content:"";display:block;width:36px;height:2px;background:var(--red);margin-top:8px}
.contact{width:330px}
.contact li{list-style:none;display:flex;align-items:center;gap:14px;font-size:13px;margin-bottom:22px}
.map-col{width:320px}
.map{width:320px;height:210px;background:linear-gradient(135deg,#e9e4d6,#d4dcc4 55%,#cfd8e0);position:relative}
.map svg{position:absolute;left:142px;top:50px}
.sitemap{flex:1}
.sitemap a{display:block;color:var(--footer-text);text-decoration:none;font-size:13px;text-transform:uppercase;padding:10px 0;border-bottom:1px solid #3a3a3a}

.bottom-bar{height:78px;background:var(--darker);display:flex;align-items:center;justify-content:space-between;padding:0 80px;font-size:12px;color:#9a9a9a}
.bottom-bar strong{color:var(--white)}
.to-top{width:34px;height:34px;border:2px solid #777;border-radius:50%;display:flex;align-items:center;justify-content:center}
</style>
</head>
<body>

<header class="site-header">
  <div class="brand">Valdessa Trucking</div>
  <nav class="main-nav">
    <a href="#">About Us</a><a href="#">Services</a><a href="#">Dispatch</a><a href="#">Equipment</a><a href="#">Safety</a><a href="#">Insurance</a><a href="#">Employment</a>
  </nav>
</header>

<section class="hero" role="img" aria-label="White Valdessa semi truck with trailer driving on a highway under a blue sky">
  <div class="hero-arrow prev"><svg width="14" height="22" viewBox="0 0 14 22"><path d="M11 2 3 11l8 9" fill="none" stroke="#fff" stroke-width="3"/></svg></div>
  <div class="hero-arrow next"><svg width="14" height="22" viewBox="0 0 14 22"><path d="M3 2l8 9-8 9" fill="none" stroke="#fff" stroke-width="3"/></svg></div>
</section>

<section class="about">
  <h2 class="section-title">VALDESSA TRUCKING LLC</h2>
  <div class="about-body">
    <div class="about-text">
      <p>Valdessa Trucking LLC was created in 2013 to assist its parent company, Valdessa Gourmet, in transporting product from our Seattle-area facility to our Northwest distribution center. Approximately four years later, Valdessa Trucking has expanded to meet the growing needs of our sister company as well as many Northwest based companies looking to transport chilled, frozen and dry product. We now operate a fleet of semis and large box trucks for local and regional distribution throughout the Pacific Northwest.</p>
      <p>Valdessa Trucking is based in Seattle, where it shares its HQ with Valdessa Gourmet. We run weekly routes to the Tri-Cities, Spokane and the interior.</p>
    </div>
    <div class="about-photo" role="img" aria-label="Worker in safety vest beside a truck loading a shipping container"></div>
  </div>
</section>

<section class="services" role="img" aria-label="Dark photo of trucks on the road behind the service icons">
  <div class="service">
    <div class="service-icon"><svg width="84" height="70" viewBox="0 0 84 70"><rect x="14" y="6" width="56" height="44" rx="6" fill="#fff"/><rect x="22" y="14" width="40" height="16" fill="#d9251d"/><rect x="18" y="50" width="12" height="12" fill="#fff"/><rect x="54" y="50" width="12" height="12" fill="#fff"/><circle cx="26" cy="40" r="4" fill="#d9251d"/><circle cx="58" cy="40" r="4" fill="#d9251d"/></svg></div>
    <h3>Trucking<br>Shipping Services</h3>
  </div>
  <div class="service">
    <div class="service-icon"><svg width="80" height="76" viewBox="0 0 80 76"><path d="M40 6 74 22v34L40 72 6 56V22z" fill="#fff"/><path d="M6 22l34 16 34-16M40 38v34" fill="none" stroke="#d9251d" stroke-width="4"/><path d="M22 14l34 16" stroke="#d9251d" stroke-width="4"/></svg></div>
    <h3>Specialty Freight &amp;<br>Shipping Services</h3>
  </div>
  <div class="service">
    <div class="service-icon"><svg width="90" height="60" viewBox="0 0 90 60"><rect x="20" y="8" width="42" height="32" fill="#fff"/><path d="M62 18h14l10 12v10H62z" fill="#fff"/><rect x="4" y="14" width="12" height="4" fill="#fff"/><rect x="0" y="24" width="16" height="4" fill="#fff"/><circle cx="32" cy="46" r="7" fill="#fff" stroke="#d9251d" stroke-width="3"/><circle cx="72" cy="46" r="7" fill="#fff" stroke="#d9251d" stroke-width="3"/></svg></div>
    <h3>Logistics<br>Management</h3>
  </div>
</section>

<section class="clients">
  <h2 class="section-title">OUR CLIENTS</h2>
  <div class="client-row">
    <span class="client">Marrow Axle</span>
    <span class="client">Delford Diesel</span>
    <span class="client">Cumbria Engines</span>
    <span class="client">Kestrel</span>
    <span class="client">Eastline</span>
    <span class="client">Benwick</span>
  </div>
</section>

<footer class="site-footer">
  <div class="footer-col contact">
    <h4>Valdessa Trucking</h4>
    <ul>
      <li><svg width="14" height="14" viewBox="0 0 14 14"><path d="M3 1l2 3-1.5 1.5a8 8 0 0 0 5 5L10 9l3 2-1 2.5C6 13 1 8 .5 2z" fill="#bdbdbd"/></svg>+1 555 010 2040</li>
      <li><svg width="12" height="16" viewBox="0 0 12 16"><path d="M6 0a6 6 0 0 1 6 6c0 4-6 10-6 10S0 10 0 6a6 6 0 0 1 6-6z" fill="#bdbdbd"/><circle cx="6" cy="6" r="2.2" fill="#222"/></svg>48 Harbor Lane, Fenmoor City, Northland</li>
      <li><svg width="16" height="12" viewBox="0 0 16 12"><rect width="16" height="12" fill="#bdbdbd"/><path d="M0 0l8 6 8-6" fill="none" stroke="#222" stroke-width="1.5"/></svg>info@valdessatrucking.example</li>
    </ul>
  </div>
  <div class="footer-col map-col">
    <h4>Find Us Here</h4>
    <div class="map" role="img" aria-label="Street map showing the company location">
      <svg width="36" height="50" viewBox="0 0 36 50"><path d="M18 0a18 18 0 0 1 18 18c0 13-18 32-18 32S0 31 0 18A18 18 0 0 1 18 0z" fill="#d9251d"/><circle cx="18" cy="18" r="7" fill="#fff"/></svg>
    </div>
  </div>
  <div class="footer-col sitemap">
    <h4>Site Map</h4>
    <a href="#">Home</a><a href="#">About Us</a><a href="#">Services</a><a href="#">Contact Us</a>
  </div>
</footer>

<div class="bottom-bar">
  <span>© 2015 <strong>VALDESSA TRUCKING</strong> ALL RIGHTS RESERVED</span>
  <span class="to-top"><svg width="14" height="10" viewBox="0 0 14 10"><path d="M1 9l6-7 6 7" fill="none" stroke="#999" stroke-width="2"/></svg></span>
</div>

</body>
</html>
```